World travel poster - I want to remember where I've been!

I would like a poster for me to print and keep in my home as a record of my world travels. It must look like a mechanical sign in an airport (see picture for example) However I am flexible with exact layout, if you'd like to add images used to enhance poster etc. I have also uploaded some pictures from my travels if you would like to use some or all of them. They are named according to location.

Poster must include:
USA 2003
Malaysia 2006
Thailand 2007
Italy 2009
India, Vietnam, Hong Kong 2010
Bali 2011
Malaysia 2012
Singapore 2012
Vietnam, Cambodia, Laos 2013
Europe 2015

and the quote:

"The world is a book and those who do not travel read only one page."
― Corwin of Veldmarsh
Updates

Hi there. I have uploaded some photos of my travels to possibly use in my poster. They are named according to location. I haven't decided if I prefer the originial layout or with images, so please post both for me to consider. Thanks so much for your time to consider my project.

Target Market(s)

Something to catch the eye of visitors and remind me of my adventures.
A classic piece that is a conversation starter.

Industry/Entity Type

Airport

Font styles to use
Other font styles liked:
• Airport mechanical font

Requirements
Must have
• Some lettering like a mechanical airport board (see image attached for example).
Dimensions that are easy to print - either A3, or a long/narrow poster.
Nice to have
• A splash of colour or an image, maybe the words 'arrivals' or 'departures'

Use of some of my pictures if it doesn't look too busy.
Should not have
• Anything too over the top.

```html
<!DOCTYPE html>
<html lang="en">
<head>
<meta charset="utf-8">
<title>Travel Departure Board</title>
<link href="https://fonts.googleapis.com/css2?family=Bebas+Neue&display=swap" rel="stylesheet">
<style>
  :root{
    --paper:#eeebe4;
    --board:#2a2a2a;
    --cell:#1c1c1c;
    --cell-line:#4a4a4a;
    --split:#0c0c0c;
    --letter:#ffffff;
    --digit:#ffe600;
    --ink:#111111;
  }
  *{box-sizing:border-box;margin:0;padding:0}
  html,body{width:849px;height:1200px;overflow:hidden;background:var(--paper)}
  .poster{
    position:relative;width:849px;height:1200px;overflow:hidden;
    background:
      radial-gradient(ellipse at center, rgba(255,255,255,0) 55%, rgba(150,110,60,.35) 100%),
      linear-gradient(160deg,#f2efe9,#e6e2da 60%,#efece6);
    box-shadow:inset 0 0 0 14px rgba(176,138,90,.55), inset 0 0 40px 20px rgba(140,100,55,.35);
    font-family:"Bebas Neue",sans-serif;
  }
  .flight-path{position:absolute;inset:0}
  .board{
    position:absolute;left:122px;top:78px;width:615px;height:995px;
    background:var(--board);border-radius:10px;
    box-shadow:0 6px 18px rgba(0,0,0,.35);
  }
  .board-head{
    position:absolute;top:22px;color:var(--digit);font-size:27px;letter-spacing:1.5px;line-height:1;
  }
  .head-dest{left:28px}
  .head-year{left:425px}
  .rows{position:absolute;left:26px;top:57px;display:flex;flex-direction:column;gap:3.8px}
  .row{display:flex;gap:22px;height:62px}
  .dest,.year{display:flex;gap:2px}
  .cell{
    position:relative;width:40px;height:62px;background:var(--cell);
    border:1px solid var(--cell-line);border-radius:2px;
    display:flex;align-items:center;justify-content:center;
    font-size:64px;line-height:1;padding-top:6px;color:var(--letter);
  }
  .cell::after{content:"";position:absolute;left:0;right:0;top:50%;height:2px;background:var(--split);opacity:.8}
  .year .cell{color:var(--digit)}
  .motto{position:absolute;left:348px;top:1099px;width:200px}
  .motto-quote{color:var(--ink);font-size:18px;line-height:17px;letter-spacing:1.4px;white-space:nowrap}
  .motto-author{display:block;font-size:7px;line-height:8px;letter-spacing:.3px;margin-top:0}
</style>
</head>
<body>
<div class="poster">
  <svg class="flight-path" width="849" height="1200" viewBox="0 0 849 1200" aria-hidden="true">
    <g fill="none" stroke="#222" stroke-width="1.3" stroke-dasharray="5 4">
      <path d="M796 80 C770 200 830 330 805 470 C785 600 830 700 805 800 C790 900 760 1000 700 1080 C660 1130 600 1135 560 1135"/>
      <path d="M78 440 C95 560 70 700 88 830 C100 940 80 1030 150 1090 C200 1130 280 1135 330 1135"/>
    </g>
    <g fill="#111">
      <g transform="translate(798 64) rotate(-40)">
        <path d="M0 -18 C3 -18 3 -14 3 -10 L3 -3 L18 5 L18 9 L3 4 L3 12 L8 16 L8 19 L0 16 L-8 19 L-8 16 L-3 12 L-3 4 L-18 9 L-18 5 L-3 -3 L-3 -10 C-3 -14 -3 -18 0 -18Z"/>
      </g>
      <g transform="translate(60 412) scale(1.45) rotate(-55)">
        <path d="M0 -18 C3 -18 3 -14 3 -10 L3 -3 L18 5 L18 9 L3 4 L3 12 L8 16 L8 19 L0 16 L-8 19 L-8 16 L-3 12 L-3 4 L-18 9 L-18 5 L-3 -3 L-3 -10 C-3 -14 -3 -18 0 -18Z"/>
      </g>
    </g>
  </svg>

  <section class="board">
    <div class="board-head head-dest">Traveled to</div>
    <div class="board-head head-year">Year</div>
    <div class="rows">
      <div class="row"><div class="dest"><span class="cell">U</span><span class="cell">S</span><span class="cell">A</span><span class="cell"></span><span class="cell"></span><span class="cell"></span><span class="cell"></span><span class="cell"></span><span class="cell"></span></div><div class="year"><span class="cell">2</span><span class="cell">0</span><span class="cell">0</span><span class="cell">3</span></div></div>
      <div class="row"><div class="dest"><span class="cell">M</span><span class="cell">A</span><span class="cell">L</span><span class="cell">A</span><span class="cell">Y</span><span class="cell">S</span><span class="cell">I</span><span class="cell">A</span><span class="cell"></span></div><div class="year"><span class="cell">2</span><span class="cell">0</span><span class="cell">0</span><span class="cell">6</span></div></div>
      <div class="row"><div class="dest"><span class="cell">T</span><span class="cell">H</span><span class="cell">A</span><span class="cell">I</span><span class="cell">L</span><span class="cell">A</span><span class="cell">N</span><span class="cell">D</span><span class="cell"></span></div><div class="year"><span class="cell">2</span><span class="cell">0</span><span class="cell">0</span><span class="cell">7</span></div></div>
      <div class="row"><div class="dest"><span class="cell">I</span><span class="cell">T</span><span class="cell">A</span><span class="cell">L</span><span class="cell">Y</span><span class="cell"></span><span class="cell"></span><span class="cell"></span><span class="cell"></span></div><div class="year"><span class="cell">2</span><span class="cell">0</span><span class="cell">0</span><span class="cell">9</span></div></div>
      <div class="row"><div class="dest"><span class="cell">I</span><span class="cell">N</span><span class="cell">D</span><span class="cell">I</span><span class="cell">A</span><span class="cell"></span><span class="cell"></span><span class="cell"></span><span class="cell"></span></div><div class="year"><span class="cell">2</span><span class="cell">0</span><span class="cell">1</span><span class="cell">0</span></div></div>
      <div class="row"><div class="dest"><span class="cell">V</span><span class="cell">I</span><span class="cell">E</span><span class="cell">T</span><span class="cell">N</span><span class="cell">A</span><span class="cell">M</span><span class="cell"></span><span class="cell"></span></div><div class="year"><span class="cell">2</span><span class="cell">0</span><span class="cell">1</span><span class="cell">0</span></div></div>
      <div class="row"><div class="dest"><span class="cell">H</span><span class="cell">O</span><span class="cell">N</span><span class="cell">G</span><span class="cell"></span><span class="cell">K</span><span class="cell">O</span><span class="cell">N</span><span class="cell">G</span></div><div class="year"><span class="cell">2</span><span class="cell">0</span><span class="cell">1</span><span class="cell">0</span></div></div>
      <div class="row"><div class="dest"><span class="cell">B</span><span class="cell">A</span><span class="cell">L</span><span class="cell">I</span><span class="cell"></span><span class="cell"></span><span class="cell"></span><span class="cell"></span><span class="cell"></span></div><div class="year"><span class="cell">2</span><span class="cell">0</span><span class="cell">1</span><span class="cell">1</span></div></div>
      <div class="row"><div class="dest"><span class="cell">M</span><span class="cell">A</span><span class="cell">L</span><span class="cell">A</span><span class="cell">Y</span><span class="cell">S</span><span class="cell">I</span><span class="cell">A</span><span class="cell"></span></div><div class="year"><span class="cell">2</span><span class="cell">0</span><span class="cell">1</span><span class="cell">2</span></div></div>
      <div class="row"><div class="dest"><span class="cell">S</span><span class="cell">I</span><span class="cell">N</span><span class="cell">G</span><span class="cell">A</span><span class="cell">P</span><span class="cell">O</span><span class="cell">R</span><span class="cell">E</span></div><div class="year"><span class="cell">2</span><span class="cell">0</span><span class="cell">1</span><span class="cell">2</span></div></div>
      <div class="row"><div class="dest"><span class="cell">V</span><span class="cell">I</span><span class="cell">E</span><span class="cell">T</span><span class="cell">N</span><span class="cell">A</span><span class="cell">M</span><span class="cell"></span><span class="cell"></span></div><div class="year"><span class="cell">2</span><span class="cell">0</span><span class="cell">1</span><span class="cell">3</span></div></div>
      <div class="row"><div class="dest"><span class="cell">C</span><span class="cell">A</span><span class="cell">M</span><span class="cell">B</span><span class="cell">O</span><span class="cell">D</span><span class="cell">I</span><span class="cell">A</span><span class="cell"></span></div><div class="year"><span class="cell">2</span><span class="cell">0</span><span class="cell">1</span><span class="cell">3</span></div></div>
      <div class="row"><div class="dest"><span class="cell">L</span><span class="cell">A</span><span class="cell">O</span><span class="cell">S</span><span class="cell"></span><span class="cell"></span><span class="cell"></span><span class="cell"></span><span class="cell"></span></div><div class="year"><span class="cell">2</span><span class="cell">0</span><span class="cell">1</span><span class="cell">3</span></div></div>
      <div class="row"><div class="dest"><span class="cell">E</span><span class="cell">U</span><span class="cell">R</span><span class="cell">O</span><span class="cell">P</span><span class="cell">E</span><span class="cell"></span><span class="cell"></span><span class="cell"></span></div><div class="year"><span class="cell">2</span><span class="cell">0</span><span class="cell">1</span><span class="cell">5</span></div></div>
    </div>
  </section>

  <footer class="motto">
    <p class="motto-quote">“The world is a book and<br>those who do not travel<br>read only one page.”<span class="motto-author">Corwin of Veldmarsh</span></p>
  </footer>
</div>
</body>
</html>
```